Tarwin Structural Approval Standards Private Assessors

Professional Construction Consultancy Company Business Card - must keep logo colours see images below - examples have been added from my last competition - please see them as examples only!

Target Market(s)

Home Builders

Industry/Entity Type

Construction

Contact Information for Business Card

See "must haves"

Font styles to use
Sans Serif

Colors
ffffff
add136
000000

Requirements
Must have
• Daniel Moravi
• Director
• Phone: 0431 587 219
• Address: 7 Tarrunga Rd,
• Hallworth Vale, SA, 5091
• Email: tarwinassessors@mailbox-example.com
• Website: www.tarwinassessors-example.com.au
• Facebook: Tarwin Structural Approval Standards
Nice to have
• Side 1: full logo
• Side 2: company details
Should not have
• hard to read
• must be clear and professional

```html
<!DOCTYPE html>
<html lang="en">
<head>
<meta charset="utf-8">
<title>Tarwin Structural Approval Standards – Business Card</title>
<link href="https://fonts.googleapis.com/css2?family=Montserrat:wght@600;700&family=Open+Sans:wght@400;600;700&display=swap" rel="stylesheet">
<style>
  :root {
    --white: #ffffff;
    --green: #add136;
    --black: #000000;
    --ink: #1d1d1d;
    --muted: #555555;
    --stage-top: #d9d9d9;
    --stage-bottom: #9a9a9a;
  }
  * { box-sizing: border-box; margin: 0; padding: 0; }
  html, body { width: 1200px; height: 960px; overflow: hidden; }
  body {
    background: radial-gradient(ellipse at 50% 40%, var(--stage-top), var(--stage-bottom));
    display: flex;
    align-items: center;
    justify-content: center;
    gap: 44px;
    font-family: "Open Sans", Arial, sans-serif;
  }
  .card {
    width: 540px;
    height: 309px;
    background: var(--white);
    box-shadow: 0 14px 34px rgba(0,0,0,0.25);
    position: relative;
  }

  /* Side 1: full name mark */
  .card-front {
    display: flex;
    align-items: center;
    justify-content: center;
  }
  .brand {
    display: flex;
    align-items: center;
    gap: 16px;
  }
  .brand-square {
    width: 52px;
    height: 52px;
    background: var(--green);
    flex: none;
  }
  .brand-name {
    font-family: "Montserrat", Arial, sans-serif;
    font-weight: 700;
    color: var(--black);
    font-size: 26px;
    line-height: 1.12;
    letter-spacing: 0.04em;
    text-transform: uppercase;
  }

  /* Side 2: company details */
  .card-back { padding: 26px 28px; }
  .card-back .brand { gap: 10px; }
  .card-back .brand-square { width: 28px; height: 28px; }
  .card-back .brand-name { font-size: 13px; line-height: 1.15; }
  .tagline {
    margin-top: 10px;
    width: 260px;
    font-size: 8.5px;
    line-height: 1.35;
    color: var(--muted);
  }
  .contact-list {
    list-style: none;
    margin-top: 16px;
    font-size: 11px;
    line-height: 1.5;
    color: var(--ink);
  }
  .contact-list li { display: flex; align-items: flex-start; gap: 7px; }
  .contact-list svg { width: 11px; height: 11px; margin-top: 3px; flex: none; fill: var(--ink); }
  .contact-web { font-weight: 700; }
  .person {
    position: absolute;
    right: 30px;
    top: 150px;
    text-align: right;
  }
  .person-name {
    font-size: 19px;
    font-weight: 600;
    color: var(--green);
  }
  .person-role {
    font-size: 8px;
    letter-spacing: 0.08em;
    color: var(--muted);
    text-transform: uppercase;
  }
  .social {
    position: absolute;
    right: 30px;
    bottom: 22px;
    text-align: right;
    font-size: 10.5px;
    color: var(--ink);
  }
  .social-line { display: flex; align-items: center; justify-content: flex-end; gap: 5px; color: var(--muted); }
  .social-square { width: 11px; height: 11px; background: var(--muted); display: inline-block; }
</style>
</head>
<body>

  <section class="card card-front" aria-label="Business card side one">
    <div class="brand">
      <span class="brand-square"></span>
      <p class="brand-name">Tarwin Structural<br>Approval Standards<br>Private Assessors</p>
    </div>
  </section>

  <section class="card card-back" aria-label="Business card side two">
    <div class="brand">
      <span class="brand-square"></span>
      <p class="brand-name">Tarwin Structural<br>Approval Standards<br>Private Assessors</p>
    </div>
    <p class="tagline">Independent Assessors of Residential and Commercial Structural Approvals for Council Development Applications</p>

    <ul class="contact-list">
      <li>
        <svg viewBox="0 0 12 12" aria-hidden="true"><path d="M1 11V4l5-3 5 3v7H7.5V7.5h-3V11z"/></svg>
        <span>7 Tarrunga Rd,<br>Hallworth Vale, SA, 5091</span>
      </li>
      <li>
        <svg viewBox="0 0 12 12" aria-hidden="true"><path d="M2.5 1l2 2.5-1.2 1.3a7 7 0 0 0 3.9 3.9L8.5 7.5 11 9.5 9.8 11C5 11 1 7 1 2.2z"/></svg>
        <span>0431 587 219</span>
      </li>
      <li>
        <svg viewBox="0 0 12 12" aria-hidden="true"><path d="M1 2.5h10v7H1zM1.6 3l4.4 3.4L10.4 3" stroke="#fff" stroke-width="0.9"/></svg>
        <span>tarwinassessors@mailbox-example.com</span>
      </li>
      <li>
        <svg viewBox="0 0 12 12" aria-hidden="true"><circle cx="6" cy="6" r="5" fill="none" stroke="#1d1d1d" stroke-width="1"/><path d="M1 6h10M6 1c-2.5 3-2.5 7 0 10M6 1c2.5 3 2.5 7 0 10" fill="none" stroke="#1d1d1d" stroke-width="0.8"/></svg>
        <span class="contact-web">www.tarwinassessors-example.com.au</span>
      </li>
    </ul>

    <div class="person">
      <p class="person-name">Daniel Moravi</p>
      <p class="person-role">Director</p>
    </div>

    <div class="social">
      <p class="social-line">Find us on <span class="social-square"></span></p>
      <p>Tarwin Structural Approval Standards</p>
    </div>
  </section>

</body>
</html>
```